Women's Health Company needs business card

We need a business card for a USA based women's health care company. We use digital technology to enhance therapy prescribed by clinicians for their patients

```html
<!DOCTYPE html>
<html lang="en">
<head>
<meta charset="utf-8">
<title>Velora Health – Business Card</title>
<link rel="stylesheet" href="https://fonts.googleapis.com/css2?family=Montserrat:wght@400;500;700&display=swap">
<style>
  :root {
    --backdrop: #d6d6d6;
    --teal: #76bfbb;
    --teal-deep: #5fb3ae;
    --purple: #8a4fa3;
    --ink: #2b2b2b;
    --paper: #ffffff;
    --rule: #9a9a9a;
  }
  * { box-sizing: border-box; margin: 0; padding: 0; }
  html, body {
    width: 1200px; height: 913px; overflow: hidden;
    background: var(--backdrop);
    font-family: "Montserrat", sans-serif;
  }
  .stage { position: relative; width: 1200px; height: 913px; }

  .card {
    position: absolute;
    width: 540px; height: 309px;
    box-shadow: 0 6px 18px rgba(0,0,0,0.18);
  }

  /* Front side */
  .card--front {
    left: 45px; top: 190px;
    background: var(--paper);
    border: 2px solid var(--teal);
    display: flex; align-items: center;
  }
  .card--front .brand {
    width: 255px;
    display: flex; justify-content: center; align-items: center; gap: 8px;
  }
  .brand__dot {
    width: 9px; height: 9px; border-radius: 50%;
    background: var(--purple);
  }
  .brand__name {
    font-weight: 500; font-size: 30px; color: var(--teal-deep);
    letter-spacing: 0.5px; white-space: nowrap;
  }
  .divider {
    width: 1px; height: 200px; background: var(--rule);
  }
  .details {
    padding-left: 26px;
    color: var(--ink);
  }
  .details__name {
    font-weight: 700; font-size: 25px; color: var(--teal-deep);
    letter-spacing: 0.3px; text-transform: uppercase; line-height: 1.1;
  }
  .details__role {
    font-size: 14px; margin: 4px 0 14px;
  }
  .contact { list-style: none; }
  .contact li {
    display: flex; align-items: center; gap: 10px;
    font-size: 13px; line-height: 22px;
  }
  .contact svg { width: 13px; height: 13px; fill: var(--purple); flex: none; }
  .address {
    font-size: 13px; line-height: 19px; margin-top: 10px;
    font-style: normal;
  }

  /* Back side */
  .card--back {
    left: 615px; top: 420px;
    background: var(--teal);
    display: flex; justify-content: center; align-items: center;
  }
  .card--back .brand__dot { background: var(--paper); width: 12px; height: 12px; }
  .card--back .brand { display: flex; align-items: center; gap: 10px; }
  .card--back .brand__name { color: var(--paper); font-size: 44px; }
</style>
</head>
<body>
<main class="stage">

  <section class="card card--front" aria-label="Business card front">
    <div class="brand">
      <span class="brand__dot"></span>
      <span class="brand__name">Velora Health</span>
    </div>
    <div class="divider"></div>
    <div class="details">
      <h1 class="details__name">Maren Ellis</h1>
      <p class="details__role">Managing Director</p>
      <ul class="contact">
        <li>
          <svg viewBox="0 0 24 24" aria-hidden="true"><path d="M6.6 10.8a15.1 15.1 0 0 0 6.6 6.6l2.2-2.2a1 1 0 0 1 1-.25 11.4 11.4 0 0 0 3.6.57 1 1 0 0 1 1 1V20a1 1 0 0 1-1 1A17 17 0 0 1 3 4a1 1 0 0 1 1-1h3.5a1 1 0 0 1 1 1c0 1.25.2 2.45.57 3.57a1 1 0 0 1-.25 1z"/></svg>
          000-000-0000
        </li>
        <li>
          <svg viewBox="0 0 24 24" aria-hidden="true"><path d="M2 5h20v14H2z M3 6l9 7 9-7" /></svg>
          Youremail@email.com
        </li>
        <li>
          <svg viewBox="0 0 24 24" aria-hidden="true"><circle cx="12" cy="12" r="10"/></svg>
          Your webadress here
        </li>
      </ul>
      <address class="address">421, Address line here<br>Country Name, 45452</address>
    </div>
  </section>

  <section class="card card--back" aria-label="Business card back">
    <div class="brand">
      <span class="brand__dot"></span>
      <span class="brand__name">Velora Health</span>
    </div>
  </section>

</main>
</body>
</html>
```